Offshore Energy Projects Management Consultancy needs a business card design

Logo available. We provide teams to deliver engineering consultancy, project management and delivery teams mainly in the offshore renewables sector. The company is all about bringing the right people to a project to deliver the scope.

The business card will be used for all staff.

The business card should be quite simple, vibrant and uncluttered but convey experience, enthusiasm and integration.

Target Market(s)

Energy Project Developers and Tier 1 construction companies

Contact Information for Business Card

Logo should be on the back of the card. I'm happy for the designer to play with the colour of the logo and background colour.

Front of the card should convey all the must have information in a clear and professional manner but without being overly traditional.

Colors

Designer to choose colors to be used in the design.

Requirements
Must have
• Land Line Tel Number, Mobile Tel Number, Email, business address, web address.

```html
<!DOCTYPE html>
<html lang="en">
<head>
<meta charset="utf-8">
<title>Seaward Delivery Partners – Business Card</title>
<link href="https://fonts.googleapis.com/css2?family=Exo+2:wght@400;500;600&display=swap" rel="stylesheet">
<style>
  :root {
    --backdrop-light: #e6e6e8;
    --backdrop-dark: #c9cacd;
    --card-white: #ffffff;
    --brand-blue: #1b8fd6;
    --brand-deep: #1164c4;
    --brand-bright: #2a9ee0;
    --ink-grey: #6d6e71;
    --rule-grey: #a7a9ac;
    --on-blue: #ffffff;
  }
  * { box-sizing: border-box; margin: 0; padding: 0; }
  html, body { width: 1200px; height: 801px; overflow: hidden; }
  body {
    background: radial-gradient(ellipse at 40% 30%, var(--backdrop-light), var(--backdrop-dark));
    font-family: "Exo 2", Arial, sans-serif;
    position: relative;
  }
  .card {
    position: absolute;
    top: 252px;
    width: 520px;
    height: 297px;
    box-shadow: 0 10px 28px rgba(0,0,0,0.22);
    overflow: hidden;
  }
  .card--front { left: 50px; background: var(--card-white); }
  .card--back { left: 630px; background: var(--brand-deep); }

  /* front */
  .brand {
    position: absolute;
    top: 40px;
    right: 40px;
    display: flex;
    align-items: center;
    gap: 10px;
    color: var(--brand-blue);
    font-weight: 600;
    font-size: 17px;
    letter-spacing: 0.6px;
    text-transform: uppercase;
  }
  .brand__dot {
    width: 14px; height: 14px; border-radius: 50%;
    background: var(--brand-blue);
  }
  .top-rule {
    position: absolute;
    top: 100px; right: 40px;
    width: 300px; height: 1px;
    background: var(--rule-grey);
  }
  .person {
    position: absolute;
    left: 34px; bottom: 36px;
    width: 170px;
  }
  .person__name {
    color: var(--brand-blue);
    font-size: 17px; font-weight: 500;
    text-transform: uppercase; letter-spacing: 0.4px;
  }
  .person__role {
    color: var(--ink-grey);
    font-size: 11px; text-transform: uppercase; letter-spacing: 0.6px;
    margin-top: 1px;
  }
  .person__rule {
    height: 1px; background: var(--rule-grey);
    margin: 9px 0 8px;
  }
  .person__address {
    color: var(--ink-grey);
    font-size: 11.5px; line-height: 1.4;
    font-style: normal;
  }
  .contacts {
    position: absolute;
    bottom: 52px;
    color: var(--ink-grey);
    font-size: 11.5px; line-height: 1.55;
    list-style: none;
  }
  .contacts--phone { left: 236px; }
  .contacts--web { left: 350px; }
  .contacts li { display: flex; align-items: center; gap: 6px; }
  .contacts svg { width: 10px; height: 10px; fill: var(--brand-blue); flex: none; }

  /* back */
  .back-pattern {
    position: absolute; inset: 0;
    background:
      radial-gradient(ellipse at 25% 20%, rgba(50,150,225,0.9), transparent 60%),
      linear-gradient(135deg, var(--brand-bright) 0%, var(--brand-deep) 100%);
  }
  .back-brand {
    position: absolute;
    right: 40px; bottom: 70px;
    display: flex; align-items: center; gap: 9px;
    color: var(--on-blue);
    font-weight: 600; font-size: 15px; letter-spacing: 0.6px;
    text-transform: uppercase;
  }
  .back-brand__dot {
    width: 12px; height: 12px; border-radius: 50%;
    background: var(--on-blue);
  }
</style>
</head>
<body>
  <section class="card card--front" aria-label="Business card front">
    <div class="brand"><span class="brand__dot"></span>Seaward Delivery Partners</div>
    <div class="top-rule"></div>

    <div class="person">
      <div class="person__name">Daniel Reyes</div>
      <div class="person__role">President</div>
      <div class="person__rule"></div>
      <address class="person__address">4120 Harbor View Road<br>Kodiak, Alaska 99615</address>
    </div>

    <ul class="contacts contacts--phone">
      <li><svg viewBox="0 0 10 10"><path d="M2 0.5 L3.6 2.6 L2.8 3.6 Q4 6 6.4 7.2 L7.4 6.4 L9.5 8 L8.3 9.5 Q4 9.3 0.5 1.7 Z"/></svg>555-214-7730</li>
      <li><svg viewBox="0 0 10 10"><path d="M2.5 0 H7.5 V10 H2.5 Z M3.5 1 V8.2 H6.5 V1 Z"/></svg>555-608-3192</li>
    </ul>

    <ul class="contacts contacts--web">
      <li><svg viewBox="0 0 10 10"><path d="M0 2 H10 V8.5 H0 Z M0.8 2.6 L5 5.6 L9.2 2.6 Z"/></svg>info@seawarddelivery.com</li>
      <li><svg viewBox="0 0 10 10"><circle cx="5" cy="5" r="4.6"/></svg>www.seawarddelivery.com</li>
    </ul>
  </section>

  <section class="card card--back" aria-label="Business card back">
    <div class="back-pattern" role="img" aria-label="Faint repeated brand pattern on blue gradient"></div>
    <div class="back-brand"><span class="back-brand__dot"></span>Seaward Delivery Partners</div>
  </section>
</body>
</html>
```